Scrum Master & Agile IT Coach Needing Business Website

Hello, my name is Brent Holloway
I am a project manger, scrum master, & agile coach. I work with IT development teams on major projects for Fortune 500 companies . My project management business has a website and can be found here: www.tq-keystride.example

I have launched a new company, ALL focused on IT Agile Coaching, I am looking to have a website created for my new company - the name of the new company is: Pins and Dials - Agile IT Coaching and Training.
I have a logo and it is provided in the materials. I like to logo; I am open to different color pallets.

The website will have a total of 7 pages; I have content for 5 of the 7 pages prepared; the other 2 pages will say under construction.

Page 1 Who am I, What I do, My Experience
Demonstrated experience and progression from Scrum Master to
Program Manager to Coach

Page 2 Pins & Dials - Agile Team Coaching
teams working major IT projects, multiple months/years

Page 3 Coaching @ the Team Level

Page 4 Coaching @ the Program Level ; LYNQ BQR level

Pages 5 -6 Under Construction

Page 7 Presentations, Slide Decks, Reference Materials

Mentor Nook need to have this highlighted somewhere Monthly Blog
Updates

Industry/Entity Type

IT development

Coding

Coded - Design and coding required

Number of Pages Required

5+ page

Requirements
Must have
• the website must be bold - I want those who visit to remember coming to my coaching site
Nice to have
• nice to have will be a modern / futuristic website; I work with IT developers, I want a website they will like
Should not have
• should not be stiff - it should be professional but fun

```html
<!DOCTYPE html>
<html lang="en">
<head>
<meta charset="utf-8">
<title>Brent Holloway – Pins &amp; Dials Agile IT Coaching</title>
<link href="https://fonts.googleapis.com/css2?family=Poppins:wght@300;400;500;600;700&display=swap" rel="stylesheet">
<style>
:root{
  --hero:#15a8c6;
  --navy:#11478a;
  --ink:#1d1d1d;
  --heading:#27456b;
  --band:#35a9e4;
  --paper:#f6f6f6;
  --footer:#15457f;
  --accent:#1fa0ea;
  --white:#ffffff;
}
*{margin:0;padding:0;box-sizing:border-box}
html,body{width:768px;height:1200px;overflow:hidden}
body{position:relative;font-family:'Poppins',sans-serif;color:var(--ink);background:var(--white)}
.abs{position:absolute}
.site-header{left:0;top:0;width:768px;height:52px;background:var(--white)}
.brand{display:flex;align-items:center;gap:6px;font-weight:700;color:var(--navy);font-size:15px;white-space:nowrap}
.brand-mark{width:12px;height:12px;background:var(--navy)}
.hero{left:0;top:52px;width:768px;height:263px;background:var(--hero);border:1px solid #0e6f85;overflow:hidden}
.hero-photo{left:400px;top:0;width:268px;height:263px;background:radial-gradient(ellipse 60% 75% at 58% 70%,#7a5e34 0%,#6e5530 40%,rgba(21,168,198,0) 78%)}
.hero-name{left:118px;top:30px;font-size:39px;font-weight:600;color:var(--white);letter-spacing:-1px;line-height:1}
.hero-role{left:120px;top:71px;font-size:14.5px;font-weight:600;color:var(--white)}
.hero-text{left:120px;top:101px;width:320px;font-size:10.2px;line-height:12px;font-weight:300;color:var(--white)}
.hero-btn{left:118px;top:174px;width:153px;height:24px;border-radius:12px;background:var(--navy);color:var(--white);font-size:10px;display:flex;align-items:center;justify-content:center}
.intro{left:104px;top:338px;width:420px;font-size:13.2px;line-height:18.5px;font-weight:300}
.section-title{left:105px;top:396px;font-size:12.3px;font-weight:500;color:var(--heading);letter-spacing:.4px;padding-bottom:5px;border-bottom:2px solid var(--heading)}
.cert{width:110px;text-align:center;font-size:8px;font-weight:500;line-height:9.5px}
.cert svg{display:block;margin:0 auto 8px}
.what-band{left:0;top:563px;width:768px;height:106px;background:var(--band);color:var(--white)}
.what-title{left:125px;top:14px;font-size:20px;font-weight:300}
.what-list{list-style:none;font-size:7.4px;font-weight:400}
.what-list li{display:flex;align-items:center;gap:8px;height:15px}
.what-list li::before{content:"";width:4px;height:4px;border:1.6px solid var(--white);border-radius:50%}
.experience{left:0;top:670px;width:768px;height:372px;background:var(--paper);border:1px solid #d0d0d0}
.exp-title{left:124px;top:22px;font-size:20px;font-weight:300}
.exp-block{left:125px;width:520px}
.exp-block h3{font-size:9.6px;font-weight:600;color:var(--navy);margin-bottom:1px}
.exp-block ul{list-style:none;font-size:7.4px;line-height:12px;font-weight:300}
.exp-block li{padding-left:15px;position:relative}
.exp-block li::before{content:"-";position:absolute;left:0}
.site-footer{left:0;top:1042px;width:768px;height:158px;background:var(--footer);color:var(--white)}
.site-footer .brand{color:var(--white);font-size:17px}
.site-footer .brand-mark{background:var(--white)}
.foot-address{left:118px;top:72px;font-size:6.5px;line-height:12px;font-weight:300}
.socials{left:118px;top:110px;display:flex;gap:14px}
.socials span{width:8px;height:8px;border-radius:50%;background:var(--white)}
.foot-head{font-size:8px;font-weight:600;letter-spacing:.2px}
.contact-lines{left:326px;top:67px;font-size:6.5px;line-height:12px;font-weight:300}
.contact-lines b{font-weight:600}
.subscribe{left:467px;top:68px;width:180px;height:20px;border-radius:10px;background:var(--white);display:flex;align-items:center}
.subscribe span{flex:1;font-size:6.5px;color:#444;padding-left:13px}
.subscribe b{width:64px;height:20px;border-radius:10px;background:var(--accent);color:var(--white);font-size:6.3px;font-weight:500;display:flex;align-items:center;justify-content:center}
.foot-rule{left:0;top:128px;width:768px;height:1px;background:rgba(255,255,255,.25)}
.copyright{left:118px;top:142px;font-size:5.3px;font-weight:300}
.foot-nav{right:120px;top:140px;display:flex;gap:10px;font-size:5.6px;font-weight:400}
</style>
</head>
<body>

<header class="site-header abs">
  <div class="brand abs" style="left:112px;top:18px"><span class="brand-mark"></span>Pins &amp; Dials</div>
</header>

<section class="hero abs">
  <div class="hero-photo abs" role="img" aria-label="Portrait photograph of Brent Holloway in a brown jacket"></div>
  <h1 class="hero-name abs">Brent Holloway</h1>
  <p class="hero-role abs">Senior Scrum Master &amp; Team Agile Coach</p>
  <p class="hero-text abs">Lorem ipsum dolor sit amet, consectetur adipiscing elit, sed do eiusmod tempor incididunt ut labore et dolore magna aliqua. Quis ipsum suspendisse ultrices gravida. Risus commodo viverra maecenas accumsan lacus vel facilisis.</p>
  <div class="hero-btn abs">Read More About Me</div>
</section>

<p class="intro abs">Lorem ipsum dolor sit amet, consectetur adipiscing elit, sed do eiusmod tempor incididunt ut</p>
<h2 class="section-title abs">COACHING DESIGNATIONS</h2>

<div class="cert abs" style="left:88px;top:448px">
  <svg width="78" height="64" viewBox="0 0 78 64"><circle cx="39" cy="32" r="30" fill="#1ea7e4"/></svg>
  <div style="padding-top:6px">CTL-PR</div>
</div>
<div class="cert abs" style="left:209px;top:448px">
  <svg width="62" height="64" viewBox="0 0 62 64"><polygon points="31,2 59,17 59,47 31,62 3,47 3,17" fill="#ffffff" stroke="#1f3e66" stroke-width="4"/></svg>
  <div>Certified Sprint<br>Basics Educator</div>
</div>
<div class="cert abs" style="left:323px;top:448px">
  <svg width="78" height="64" viewBox="0 0 78 64"><circle cx="39" cy="34" r="29" fill="#f6a93b"/><rect x="2" y="27" width="74" height="14" fill="#f08a24"/></svg>
  <div style="padding-top:6px">ITC-ACP</div>
</div>
<div class="cert abs" style="left:440px;top:448px">
  <svg width="76" height="68" viewBox="0 0 76 68"><polygon points="38,1 75,34 38,67 1,34" fill="#1f3e66"/></svg>
  <div>LYNQ Advanced<br>Scrum Master</div>
</div>
<div class="cert abs" style="left:558px;top:448px">
  <svg width="74" height="64" viewBox="0 0 74 64"><circle cx="37" cy="32" r="29" fill="#f9b73a"/></svg>
  <div style="padding-top:6px">A-CTL</div>
</div>

<section class="what-band abs">
  <h2 class="what-title abs">What I do</h2>
  <ul class="what-list abs" style="left:132px;top:50px">
    <li>Sr. Scrum Master</li>
    <li>Advanced LYNQ Scrum Master</li>
  </ul>
  <ul class="what-list abs" style="left:326px;top:50px">
    <li>Hybrid Scrum Master/ Project Manager</li>
    <li>Program Manager</li>
  </ul>
  <ul class="what-list abs" style="left:547px;top:50px">
    <li>Business Transformation</li>
  </ul>
</section>

<section class="experience abs">
  <h2 class="exp-title abs">What is My Experience</h2>
  <div class="exp-block abs" style="top:68px">
    <h3>As a LYNQ Adv Scrum Master, I:</h3>
    <ul>
      <li>stand up teams</li>
      <li>run development efforts concurrently leading multiple teams</li>
      <li>run LYNQ ceremonies</li>
      <li>Scrum of Scrums facilitator</li>
      <li>PI Planning team facilitator (multiple teams on BQR)</li>
      <li>Teach and coach to advanced development team strategies</li>
      <li>Lead program level communications and business status updates on behalf of the team</li>
    </ul>
  </div>
  <div class="exp-block abs" style="top:176px">
    <h3>As a Hybrid Scrum Master / Project Manager, I:</h3>
    <ul>
      <li>standup teams</li>
      <li>run multiple program level projects simultaneously</li>
      <li>implement custom hybrid development strategies</li>
      <li>manage to project triple constraints</li>
      <li>communications lead and business liaison</li>
      <li>use multiple coaching styles based on team and project</li>
    </ul>
  </div>
  <div class="exp-block abs" style="top:272px">
    <h3>Business Transformation Program Manager</h3>
    <ul>
      <li>lead business transformation efforts at the program level</li>
      <li>work with multiple product owners, business analysts, and business stakeholders on requirements</li>
      <li>lead the international rollout, onboarding, and support of new transformational CRM tool, Ledgerline</li>
      <li>standup and lead multi-functional teams consisting of business and technology team members</li>
      <li>Serve as program organization and communications lead</li>
    </ul>
  </div>
</section>

<footer class="site-footer abs">
  <div class="brand abs" style="left:108px;top:30px"><span class="brand-mark"></span>Pins &amp; Dials</div>
  <p class="foot-address abs">48 Marrow Lane, Suite 210, Room 12<br>FL 300417</p>
  <div class="socials abs" aria-label="Social links"><span></span><span></span><span></span><span></span></div>
  <h4 class="foot-head abs" style="left:326px;top:48px">CONTACT ME</h4>
  <p class="contact-lines abs"><b>P:</b> +21 5550 1842<br><b>F:</b> +21 5550 7316<br><span style="display:block;height:3px"></span><b>E:</b> hello@pinsdials.example<br><b>W:</b> www.pinsdials.example</p>
  <h4 class="foot-head abs" style="left:473px;top:45px">SUBSCRIBE NEWSLETTER</h4>
  <div class="subscribe abs"><span>Email Address</span><b>SUBSCRIBE</b></div>
  <div class="foot-rule abs"></div>
  <p class="copyright abs">copyright 2022, All Rights Reserved, Pins &amp; Dials LLC</p>
  <nav class="foot-nav abs">
    <span>About Me</span><span>My Experience</span><span>Pins &amp; Dials - Agile Team</span><span>Coaching</span><span>Why is Pins &amp; Dials here</span><span>Contact</span>
  </nav>
</footer>

</body>
</html>
```